Residential Construction Business - Site Signage

I need a design made for a site fence banner. We have a logo and branding so the design would need to be aligned with this. It would need to be made to specific size ratio so that it can be sent to the maker for production.
ratio : 4600 wide x 1700 high
The design should feature our website and also the slogan
"Stay Put, Transform It"

Target Market(s)

potential clients

Industry/Entity Type

construction

Font styles to use
Other font styles liked:
• to match branding

Colors
0054AA
0677BA
7BADD7
CADEEF
E8F1F8

Requirements
Must have
• www.velmbuild.com.au Majority of the sign is our brand logo
Nice to have
• Majority of the sign is our brand logo
Should not have
• colors and themes that arent brand relevant

```html
<!DOCTYPE html>
<html lang="en">
<head>
<meta charset="UTF-8">
<title>Velm Build – Site Fence Banner</title>
<link rel="stylesheet" href="https://fonts.googleapis.com/css2?family=Montserrat:wght@300;400;500&display=swap">
<style>
  :root {
    --page-bg: #f4f2ef;
    --navy: #0c3a5a;
    --panel-light: #e8f1f8;
    --brand-blue: #0677ba;
    --text-grey: #3c4650;
  }
  html, body {
    margin: 0;
    padding: 0;
    width: 1200px;
    height: 1125px;
    overflow: hidden;
    background: var(--page-bg);
  }
  .canvas {
    position: relative;
    width: 1200px;
    height: 1125px;
  }
  .fence-banner {
    position: absolute;
    left: 50px;
    top: 359px;
    width: 1100px;
    height: 407px;
    background: var(--panel-light);
    box-shadow: 0 10px 18px rgba(0, 0, 0, 0.22);
    overflow: hidden;
    font-family: "Montserrat", sans-serif;
  }
  .banner-chevron {
    position: absolute;
    inset: 0;
    width: 100%;
    height: 100%;
  }
  .brand-name {
    position: absolute;
    right: 209px;
    top: 174px;
    margin: 0;
    font-size: 48px;
    font-weight: 500;
    letter-spacing: 0.2em;
    margin-right: -0.2em;
    line-height: 1;
    color: var(--navy);
    white-space: nowrap;
  }
  .slogan {
    position: absolute;
    right: 214px;
    top: 244px;
    margin: 0;
    font-size: 25px;
    font-weight: 400;
    line-height: 1.2;
    color: var(--brand-blue);
    white-space: nowrap;
  }
  .website {
    position: absolute;
    left: 574px;
    top: 329px;
    margin: 0;
    padding-left: 18px;
    border-left: 3px solid var(--brand-blue);
    font-size: 21px;
    font-weight: 300;
    line-height: 36px;
    color: var(--text-grey);
    white-space: nowrap;
  }
</style>
</head>
<body>
  <main class="canvas">
    <section class="fence-banner" aria-label="Velm Build site fence banner">
      <svg class="banner-chevron" viewBox="0 0 1100 407" preserveAspectRatio="none" aria-hidden="true">
        <polygon points="0,0 540,0 369,203 540,407 0,407" fill="var(--navy)"/>
      </svg>
      <h1 class="brand-name">VELM BUILD</h1>
      <p class="slogan">Stay Put, Transform It</p>
      <p class="website">www.velmbuild.com.au</p>
    </section>
  </main>
</body>
</html>
```